Business Card Design Project

We need a business card design for a management consultancy focused on financial innovation and digital money, run by experts from the Financial Services, Telecoms and Money Transfer industries.
Our products include services such as Mobile Payments, Mobile Money, Digital Wallets, Online Payments, Branchless Banking and more. We work with regulatory information, business plans, financial modelling, strategic planning, new products functional specification, new technologies evaluation, etc.
See company logo attached.
We would like to see 2 versions: one in portuguese and one in english (regarding data information). You can see below information needed (whenever there is a difference between the two versions, the first one is in english and the second one in portuguese).

Name
Position
Phone/ Tel: ++55-11-xxxx-xxxx
Cell/ Cel: ++55-11-9 xxxx-xxxx
Dr. Morvelo Tastran Av., 512 - Tower II - 16th floor / Avenida Dr. Morvelo Tastran, 512 - Torre II - 16o. andar
São Paulo - SP
07219-316 - Brazil/ 07219-316 - Brasil

Target Market(s)

Audience: C-level executives from banks, credit card companies, acquirers, IT developers, retailers

Industry/Entity Type

Financial

Requirements
Must have
• Must use the logo and information above. Front must have white background. Back side should have only logo.
Nice to have
• Back should be in another colour but if it seems too exxagerated, maintain back in white also.
Should not have
• Do not add other illustrations to the business card.

```html
<!DOCTYPE html>
<html lang="en">
<head>
<meta charset="utf-8">
<title>R Valdmann – Business Card</title>
<link rel="stylesheet" href="https://fonts.googleapis.com/css2?family=Lato:wght@300;400;700;900&display=swap">
<style>
  :root {
    --backdrop: #5ecfbe;
    --card-white: #ffffff;
    --panel-grey: #dcdcdf;
    --navy: #1c2a5c;
    --ink: #2b2f3a;
    --rule: #9a9aa2;
  }
  * { box-sizing: border-box; margin: 0; padding: 0; }
  html, body {
    width: 1200px; height: 836px; overflow: hidden;
    background: var(--backdrop);
    font-family: "Lato", sans-serif;
  }
  .canvas {
    position: relative; width: 1200px; height: 836px;
    display: flex; align-items: center; justify-content: center; gap: 60px;
  }
  .card {
    position: relative; width: 520px; height: 297px;
    background: var(--card-white);
    box-shadow: 0 14px 30px rgba(0,0,0,.18);
    overflow: hidden; color: var(--ink);
  }
  .card-front .panel { position: absolute; inset: 0; }

  .holder { position: absolute; right: 32px; top: 30px; text-align: right; }
  .holder-name { font-size: 24px; font-weight: 400; letter-spacing: .5px; color: var(--navy); text-transform: uppercase; line-height: 1.1; }
  .holder-name strong { font-weight: 900; }
  .holder-role { font-size: 11px; letter-spacing: 2px; text-transform: uppercase; margin-top: 6px; color: var(--ink); }

  .contact { position: absolute; right: 32px; top: 108px; display: flex; gap: 14px; }
  .contact-block { display: flex; gap: 9px; align-items: flex-start; font-size: 10px; line-height: 1.55; white-space: nowrap; }
  .contact-block + .contact-block { border-left: 1px solid var(--rule); padding-left: 14px; }
  .icon-tile { width: 28px; height: 28px; background: var(--navy); flex: none; display: flex; align-items: center; justify-content: center; }

  .brand { position: absolute; display: flex; align-items: center; gap: 10px; }
  .brand-mark { width: 22px; height: 22px; background: var(--navy); flex: none; }
  .brand-name { font-size: 22px; font-weight: 400; letter-spacing: 1px; color: var(--navy); text-transform: uppercase; line-height: 1; }
  .brand-tag { font-size: 9px; letter-spacing: 1.6px; color: var(--ink); text-transform: uppercase; margin-top: 4px; white-space: nowrap; }
  .card-front .brand { left: 30px; bottom: 34px; }

  .card-back .band { position: absolute; left: 0; right: 0; height: 16px; background: var(--navy); }
  .card-back .band-top { top: 62px; }
  .card-back .band-bottom { bottom: 62px; }
  .card-back .brand { left: 50%; top: 50%; transform: translate(-50%, -50%); }
</style>
</head>
<body>
<main class="canvas">
  <section class="card card-front" aria-label="Card front">
    <svg class="panel" viewBox="0 0 520 297" preserveAspectRatio="none" aria-hidden="true">
      <polygon points="140,0 520,0 520,297 320,297 260,180 0,180 0,0" fill="var(--panel-grey)"/>
    </svg>
    <div class="holder">
      <p class="holder-name"><strong>Marcus</strong> Hollend</p>
      <p class="holder-role">Position</p>
    </div>
    <div class="contact">
      <div class="contact-block">
        <span class="icon-tile">
          <svg width="17" height="17" viewBox="0 0 24 24" aria-hidden="true"><path d="M3 11 12 3l9 8h-3v9h-5v-6h-2v6H6v-9z" fill="#fff"/></svg>
        </span>
        <p>Dr. Morvelo Tastran Av.,<br>512 - Tower II - 16th floor<br>São Paulo - SP<br>07219-316 - Brazil</p>
      </div>
      <div class="contact-block">
        <span class="icon-tile">
          <svg width="17" height="17" viewBox="0 0 24 24" aria-hidden="true"><path d="M6.6 10.8a15 15 0 0 0 6.6 6.6l2.2-2.2c.3-.3.7-.4 1-.2 1.1.4 2.3.6 3.6.6.6 0 1 .4 1 1V20c0 .6-.4 1-1 1A17 17 0 0 1 3 4c0-.6.4-1 1-1h3.5c.6 0 1 .4 1 1 0 1.3.2 2.5.6 3.6.1.3 0 .7-.2 1z" fill="#fff"/></svg>
        </span>
        <p>Phone: ++55-11-xxxx-xxxx<br>Cell: ++55-11-9 xxxx-xxxx</p>
      </div>
    </div>
    <div class="brand">
      <span class="brand-mark"></span>
      <div>
        <p class="brand-name">R Valdmann</p>
        <p class="brand-tag">Management Consulting</p>
      </div>
    </div>
  </section>

  <section class="card card-back" aria-label="Card back">
    <div class="band band-top"></div>
    <div class="band band-bottom"></div>
    <div class="brand">
      <span class="brand-mark"></span>
      <div>
        <p class="brand-name">R Valdmann</p>
        <p class="brand-tag">Consultoria Estratégica</p>
      </div>
    </div>
  </section>
</main>
</body>
</html>
```